Global social media analytics company needs business card design

We need an updated business card design to align with our new website - plumvantix.com -

I would also like a favicon designed as well.

Target Market(s)

CEOs, CMOs go big companies

Industry/Entity Type

Business

Contact Information for Business Card

Room for the following:
Address
Main telephone
Direct telephone or cell phone
twitter handle

Colors
aaaaaa

Requirements
Must have
• Attention to detail; style.
• Use the logo color from our website - which is gray

```html
<!DOCTYPE html>
<html lang="en">
<head>
<meta charset="utf-8">
<title>Plumvantix Business Card</title>
<link rel="stylesheet" href="https://fonts.googleapis.com/css2?family=Open+Sans:wght@600;700&display=swap">
<style>
  :root {
    --bg: #d9d2c7;
    --card: #ffffff;
    --ink: #3a3d3c;
    --accent-grey: #aaaaaa;
    --social: #1f7bc1;
  }
  * { margin: 0; padding: 0; box-sizing: border-box; }
  html, body { width: 1200px; height: 857px; overflow: hidden; }
  body {
    position: relative;
    background: var(--bg);
    font-family: "Open Sans", Arial, sans-serif;
    color: var(--ink);
  }
  .card {
    position: absolute;
    width: 680px;
    height: 430px;
    border-radius: 22px;
    overflow: hidden;
  }
  /* Front */
  .card-front { left: 44px; top: 50px; background: var(--card); }
  .brand {
    position: absolute;
    left: 52px; top: 44px;
    display: flex; align-items: center; gap: 18px;
  }
  .brand-dot {
    width: 112px; height: 112px; border-radius: 50%;
    background: var(--ink);
  }
  .brand-name {
    font-weight: 700;
    font-size: 56px;
    letter-spacing: -1px;
    color: var(--ink);
  }
  .company {
    position: absolute; left: 58px; top: 196px;
    font-weight: 700; font-size: 25px; letter-spacing: 0.3px;
  }
  .contact-list {
    position: absolute; left: 58px; top: 246px;
    list-style: none;
  }
  .contact-item {
    display: flex; align-items: flex-start; gap: 12px;
    font-weight: 600; font-size: 18px; line-height: 20px;
    margin-bottom: 12px;
  }
  .contact-item:last-child { margin-bottom: 0; }
  .contact-item .icon { width: 20px; height: 20px; flex: 0 0 20px; }
  .contact-item .lines { line-height: 19px; }
  .social-square { display: block; background: var(--social); }

  /* Back */
  .card-back { left: 456px; top: 380px; background: transparent; }
  .band { position: absolute; left: 0; width: 100%; background: var(--ink); }
  .band-top { top: 0; height: 180px; }
  .band-bottom { top: 272px; height: 158px; }
  .back-brand {
    position: absolute; left: 0; right: 0; top: 187px;
    display: flex; justify-content: center; align-items: center; gap: 12px;
  }
  .back-brand .brand-dot { width: 78px; height: 78px; }
  .back-brand .brand-name { font-size: 38px; }
  .web {
    position: absolute; left: 0; right: 0; top: 298px;
    text-align: center;
    color: var(--card);
    font-weight: 700; font-size: 17px; letter-spacing: 3px;
  }
</style>
</head>
<body>
  <section class="card card-front">
    <div class="brand">
      <div class="brand-dot"></div>
      <span class="brand-name">plumvantix</span>
    </div>
    <h1 class="company">PLUMVANTIX, INC.</h1>
    <ul class="contact-list">
      <li class="contact-item">
        <svg class="icon" viewBox="0 0 20 20"><rect width="20" height="20" rx="3" fill="var(--ink)"/><path d="M10 4a4 4 0 0 0-4 4c0 3 4 8 4 8s4-5 4-8a4 4 0 0 0-4-4zm0 5.5a1.5 1.5 0 1 1 0-3 1.5 1.5 0 0 1 0 3z" fill="#fff"/></svg>
        <span class="lines">418 Linden Crest Ave. 4th Fl<br>Millbrook, NY 12545, USA</span>
      </li>
      <li class="contact-item">
        <svg class="icon" viewBox="0 0 20 20"><rect width="20" height="20" rx="3" fill="var(--ink)"/><path d="M6 4l2.5 0 1 3-1.5 1.2a8 8 0 0 0 3.8 3.8L13 10.5l3 1V14a1.5 1.5 0 0 1-1.5 1.5A10.5 10.5 0 0 1 4.5 5.5 1.5 1.5 0 0 1 6 4z" fill="#fff"/></svg>
        <span>+1 555 014 2760</span>
      </li>
      <li class="contact-item">
        <svg class="icon" viewBox="0 0 20 20"><rect x="1.5" y="4" width="17" height="12" fill="none" stroke="var(--ink)" stroke-width="1.5"/><path d="M1.5 4l8.5 7 8.5-7M1.5 16l6-5.5M18.5 16l-6-5.5" fill="none" stroke="var(--ink)" stroke-width="1.5"/></svg>
        <span>info@plumvantix.com</span>
      </li>
      <li class="contact-item">
        <svg class="icon" viewBox="0 0 20 20"><g fill="none" stroke="var(--ink)" stroke-width="1.4"><circle cx="10" cy="10" r="8"/><ellipse cx="10" cy="10" rx="3.5" ry="8"/><path d="M2 10h16M3.5 6h13M3.5 14h13"/></g></svg>
        <span>www.plumvantix.com</span>
      </li>
      <li class="contact-item">
        <span class="icon social-square"></span>
        <span>Plumvantix, Inc.</span>
      </li>
    </ul>
  </section>

  <section class="card card-back">
    <div class="band band-top"></div>
    <div class="back-brand">
      <div class="brand-dot"></div>
      <span class="brand-name">plumvantix</span>
    </div>
    <div class="band band-bottom"></div>
    <p class="web">www.plumvantix.com</p>
  </section>
</body>
</html>
```